Poster Design Project

Poster with modern feeling to be displayed in office. The text that needs to be included in this poster is below:

Rules
1. If it’s not in writing it doesn’t exist.
2. No such thing as 'off the record.'
3. Do not hold a private conversation in a public place.
4. Don’t believe any number that ends in zero.
5. Never turn down an opportunity to eat or go to the bathroom.
6. Don’t spend any of your own money. Don’t even admit you own a credit card. Don’t spend money that is not yours.
7. Not always a 'right' or 'wrong' answer - 'It depends.'
8. In a campaign, someone has to be in charge – campaigns are a place to foster democracy, not practice it.
9. Assume nothing.
10. If you make a mistake, fix it before analyzing. Bad news doesn’t age well.

Industry/Entity Type

Credit Card

Requirements
Must have
• Rules
7. Not always a “right” or “wrong” answer - 'It depends.' 
9. Assume nothing.

```html
<!DOCTYPE html>
<html lang="en">
<head>
<meta charset="utf-8">
<title>Office Rules Poster</title>
<link rel="stylesheet" href="https://fonts.googleapis.com/css2?family=Quicksand:wght@500&family=Lilita+One&display=swap">
<style>
  :root {
    --page: #ffffff;
    --sheet: #f3f3f3;
    --bar: #464646;
    --ink: #ffffff;
    --numeral: #9b9b9b;
  }
  * { margin: 0; padding: 0; box-sizing: border-box; }
  html, body { width: 1200px; height: 1000px; overflow: hidden; background: var(--page); }
  .canvas { position: relative; width: 1200px; height: 1000px; }
  .poster {
    position: absolute; left: 290px; top: 35px; width: 652px; height: 920px;
    background: var(--sheet);
  }
  .rules { list-style: none; position: absolute; left: 17px; top: 17px; width: 617px; }
  .rule {
    position: relative; height: 82px; margin-bottom: 6.8px;
    background: var(--bar); border-radius: 3px; overflow: hidden;
    display: flex; align-items: center;
  }
  .rule-icon {
    position: absolute; left: 12px; top: 50%; transform: translateY(-50%);
    width: 80px; height: 70px; display: flex; align-items: center; justify-content: center;
  }
  .rule-icon svg { display: block; }
  .rule-text {
    position: relative; z-index: 2;
    margin-left: 107px; width: 438px;
    font-family: "Quicksand", sans-serif; font-weight: 500; font-size: 17px;
    line-height: 1.35; color: var(--ink); letter-spacing: -0.3px;
  }
  .rule-number {
    position: absolute; right: 8px; top: 50%; transform: translateY(-50%) skewX(-10deg);
    font-family: "Lilita One", sans-serif; font-weight: 400; font-style: normal;
    font-size: 72px; line-height: 1; letter-spacing: -2px;
    color: var(--numeral); z-index: 1;
  }
</style>
</head>
<body>
<div class="canvas">
  <main class="poster">
    <ol class="rules">
      <li class="rule">
        <span class="rule-icon"><svg width="66" height="66" viewBox="0 0 66 66" fill="none" stroke="#fff" stroke-width="4"><rect x="4" y="8" width="54" height="54" rx="6"/><path d="M20 48l4-12 26-26 8 8-26 26z" fill="#464646"/><path d="M24 36l8 8M46 14l8 8"/></svg></span>
        <p class="rule-text">If it’s not in writing it doesn’t exist.</p>
        <span class="rule-number">1</span>
      </li>
      <li class="rule">
        <span class="rule-icon"><svg width="82" height="62" viewBox="0 0 82 62" stroke="#fff" stroke-width="4" fill="#464646"><path d="M6 6l16-2 56 48-14 6z"/><path d="M76 6l-16-2-56 48 14 6z"/></svg></span>
        <p class="rule-text">No such thing as 'off the record.'</p>
        <span class="rule-number">2</span>
      </li>
      <li class="rule">
        <span class="rule-icon"><svg width="76" height="62" viewBox="0 0 76 62" fill="#fff"><ellipse cx="27" cy="32" rx="24" ry="17"/><path d="M10 42l-4 16 16-10z"/><ellipse cx="55" cy="20" rx="19" ry="14" stroke="#464646" stroke-width="3"/><path d="M64 30l8 14-14-8z"/></svg></span>
        <p class="rule-text">Do not hold a private conversation in a<br>public place.</p>
        <span class="rule-number">3</span>
      </li>
      <li class="rule">
        <span class="rule-icon"><svg width="70" height="70" viewBox="0 0 70 70" fill="none" stroke="#fff"><circle cx="35" cy="35" r="31" stroke-width="5"/><ellipse cx="35" cy="35" rx="10" ry="17" stroke-width="6"/><path d="M27 46l16-22" stroke-width="3"/></svg></span>
        <p class="rule-text">Don’t believe any number that ends in zero.</p>
        <span class="rule-number">4</span>
      </li>
      <li class="rule">
        <span class="rule-icon"><svg width="86" height="62" viewBox="0 0 86 62" fill="#fff"><path d="M4 4h3v18h3V4h3v18h3V4h3v20c0 5-3 8-6 9v27h-6V33c-3-1-6-4-6-9z"/><ellipse cx="33" cy="14" rx="7" ry="11"/><rect x="30" y="22" width="6" height="38"/><rect x="76" y="6" width="8" height="26" rx="1"/><path d="M44 30h40c0 12-8 18-16 19l2 11H56l2-11c-8-2-14-8-14-19z"/></svg></span>
        <p class="rule-text">Never turn down an opportunity to eat or<br>go to the bathroom.</p>
        <span class="rule-number">5</span>
      </li>
      <li class="rule">
        <span class="rule-icon"><svg width="52" height="66" viewBox="0 0 52 66"><path d="M14 2l6 6 6-6 6 6 6-6-4 14H18z" fill="#fff"/><path d="M19 18h14c12 8 18 20 18 30 0 12-10 16-25 16S1 60 1 48c0-10 6-22 18-30z" fill="#fff"/><text x="26" y="56" text-anchor="middle" font-family="Quicksand, sans-serif" font-size="28" font-weight="700" fill="#464646">$</text></svg></span>
        <p class="rule-text">Don’t spend any of your own money. Don’t even admit you own a credit card. Don’t spend money that is not yours.</p>
        <span class="rule-number">6</span>
      </li>
      <li class="rule">
        <span class="rule-icon"><svg width="84" height="70" viewBox="0 0 84 70" fill="none" stroke="#fff" stroke-width="4"><circle cx="22" cy="26" r="18"/><path d="M12 24l9 12 22-30" stroke-width="6"/><circle cx="60" cy="48" r="18"/><path d="M51 40l18 16M69 40L51 56" stroke-width="6"/></svg></span>
        <p class="rule-text">Not always a “right” or “wrong” answer - 'It depends.'</p>
        <span class="rule-number">7</span>
      </li>
      <li class="rule">
        <span class="rule-icon"><svg width="76" height="70" viewBox="0 0 76 70" fill="#fff"><circle cx="14" cy="11" r="9"/><circle cx="38" cy="11" r="9"/><circle cx="62" cy="11" r="9"/><path d="M2 22h24v30l-6 16h-12L2 52z"/><path d="M26 22h24v30l-6 16H32L26 52z" stroke="#464646" stroke-width="2"/><path d="M50 22h24v30l-6 16H56L50 52z"/></svg></span>
        <p class="rule-text">In a campaign, someone has to be in charge – campaigns are a place to foster democracy, not practice it.</p>
        <span class="rule-number">8</span>
      </li>
      <li class="rule">
        <span class="rule-icon"><svg width="68" height="66" viewBox="0 0 68 66" fill="#fff"><circle cx="20" cy="24" r="14"/><circle cx="36" cy="16" r="14"/><circle cx="52" cy="26" r="13"/><circle cx="44" cy="38" r="12"/><circle cx="26" cy="38" r="12"/><circle cx="14" cy="52" r="5"/><circle cx="8" cy="61" r="3"/></svg></span>
        <p class="rule-text">Assume nothing.</p>
        <span class="rule-number">9</span>
      </li>
      <li class="rule">
        <span class="rule-icon"><svg width="80" height="66" viewBox="0 0 80 66" fill="#fff"><path d="M10 4h26l4 6-8 4-5-3-4 4 44 44-6 6L17 21l-4 4-9-9z"/><path d="M70 2a14 14 0 0 0-16 18L10 56l6 6 36-42a14 14 0 0 0 18-16l-8 8-7-3-1-7z"/></svg></span>
        <p class="rule-text">If you make a mistake, fix it before analyzing. Bad news doesn’t age well.</p>
        <span class="rule-number">10</span>
      </li>
    </ol>
  </main>
</div>
</body>
</html>
```